LOS PINOS DE ARENA - EXCLUSIVE AND LUXURY REAL ESTATE PROJECT

Se trata del diseño de un mono poste grande (4 m x 2 m) o (8m x 3m) anunciando la construcción de 30 villas de lujo en un terreno en primera línea de playa en el sur de España (Cádiz).

La idea es crear expectación y transmitir lujo y exclusividad.

Target Market(s)

Clientes de alto poder adquisitivo que quieran adquirir su segunda vivienda en un entorno privilegiado a escasos pasos de una de las playas más bonitas de Cádiz.

Industry/Entity Type

REAL ESTATE

Colors

Designer to choose colors to be used in the design.

Requirements
Must have
• LOS PINOS DE ARENA as the name of the development
Nice to have
• Crear expectación con ideas del tipo: “Coming soon” o “No te lo puedes perder”

```html
<!DOCTYPE html>
<html lang="es">
<head>
<meta charset="utf-8">
<title>Los Pinos de Arena – Villas de lujo</title>
<link rel="stylesheet" href="https://fonts.googleapis.com/css2?family=Bebas+Neue&family=Montserrat:wght@500;600&display=swap">
<style>
  :root {
    --blue: #0a4fb0;
    --blue-dark: #0b3f86;
    --blue-soft: #4a72c4;
    --yellow: #f0b21d;
    --ink: #1c1c1c;
    --white: #ffffff;
    --backdrop: #d6d6d6;
  }
  * { margin: 0; padding: 0; box-sizing: border-box; }
  html, body {
    width: 1200px; height: 863px; overflow: hidden;
    background: var(--backdrop);
  }
  .billboard {
    position: absolute; left: 0; top: 132px;
    width: 1200px; height: 599px;
    background: var(--white);
    overflow: hidden;
  }
  .billboard-art { position: absolute; inset: 0; width: 1200px; height: 599px; }
  .headline {
    position: absolute; left: 37px; top: 30px;
    font-family: "Bebas Neue", sans-serif;
    font-size: 69px; line-height: 1; letter-spacing: 0.5px;
    color: var(--blue); white-space: nowrap;
  }
  .headline-rule {
    position: absolute; left: 37px; top: 107px; width: 424px; height: 2px;
    background: var(--blue);
  }
  .headline-rule::before {
    content: ""; position: absolute; left: 0; top: -2px; width: 212px; height: 6px;
    background: var(--blue-soft);
  }
  .intro {
    position: absolute; left: 37px; top: 130px; width: 424px;
    font-family: "Montserrat", sans-serif; font-weight: 600;
    font-size: 18.5px; line-height: 29px; color: var(--ink);
    text-align: justify; text-align-last: justify; letter-spacing: 0.4px;
  }
  .intro span { display: block; text-align: justify; text-align-last: justify; }
  .urgency-band {
    position: absolute; left: 0; top: 230px; width: 504px; height: 63px;
    background: linear-gradient(90deg, var(--blue-dark), var(--blue));
  }
  .urgency-band p {
    position: absolute; left: 37px; top: 6px;
    font-family: "Bebas Neue", sans-serif; font-size: 56px; line-height: 1;
    color: var(--white); white-space: nowrap;
  }
  .details {
    position: absolute; left: 41px; top: 312px; width: 440px;
    font-family: "Montserrat", sans-serif; font-weight: 500;
    font-size: 17.5px; line-height: 27px; color: var(--ink);
  }
  .contact-box {
    position: absolute; left: 36px; top: 385px; width: 374px; height: 50px;
    border: 1.5px solid var(--yellow); border-radius: 8px;
    display: flex; align-items: center; padding-left: 20px; gap: 16px;
    font-family: "Bebas Neue", sans-serif; font-size: 42px; line-height: 1;
  }
  .contact-label { color: var(--blue); }
  .contact-number { display: flex; align-items: center; gap: 8px; color: var(--ink); }
  .contact-number svg { width: 26px; height: 26px; }
</style>
</head>
<body>
  <section class="billboard">
    <svg class="billboard-art" viewBox="0 0 1200 599" xmlns="http://www.w3.org/2000/svg">
      <defs>
        <linearGradient id="coastTones" x1="0" y1="0" x2="0" y2="1">
          <stop offset="0" stop-color="#3fa0e2"/>
          <stop offset="0.45" stop-color="#e2c89a"/>
          <stop offset="0.72" stop-color="#7f8566"/>
          <stop offset="0.85" stop-color="#d8c9a4"/>
          <stop offset="1" stop-color="#6fa8b8"/>
        </linearGradient>
        <linearGradient id="villaTones" x1="0" y1="0" x2="0" y2="1">
          <stop offset="0" stop-color="#3d6fc4"/>
          <stop offset="0.25" stop-color="#f1f1f1"/>
          <stop offset="0.6" stop-color="#c9c5bd"/>
          <stop offset="1" stop-color="#ece9e3"/>
        </linearGradient>
        <linearGradient id="poolTones" x1="0" y1="0" x2="0" y2="1">
          <stop offset="0" stop-color="#3b6fc8"/>
          <stop offset="0.35" stop-color="#eeeeee"/>
          <stop offset="0.55" stop-color="#c8c0ae"/>
          <stop offset="0.68" stop-color="#5ccbe2"/>
          <stop offset="0.82" stop-color="#7c5e48"/>
          <stop offset="1" stop-color="#ececec"/>
        </linearGradient>
      </defs>

      <rect x="0" y="0" width="1200" height="599" fill="url(#coastTones)" role="img" aria-label="Foto de la playa de Cádiz con rocas, paseo marítimo, palmeras y edificios"/>

      <path class="wave-accent" d="M0 0 H1200 V12 C1080 18 1010 40 960 60 L760 420 C600 520 320 510 0 470 Z" fill="var(--yellow)"/>
      <path class="wave-panel" d="M0 0 H1200 V10 C1080 14 1010 36 960 56 L740 400 C590 480 320 470 0 453 Z" fill="var(--white)"/>

      <path class="corner-swoosh" d="M995 48 C1070 22 1140 12 1200 10 V110 C1160 110 1110 118 1070 132 Z" fill="var(--yellow)"/>

      <circle cx="693" cy="260" r="203" fill="var(--yellow)"/>
      <circle cx="700" cy="262" r="190" fill="url(#villaTones)" role="img" aria-label="Render de villa moderna blanca con salón acristalado y terraza"/>

      <circle cx="945" cy="201" r="159" fill="var(--white)"/>
      <circle cx="945" cy="201" r="147" fill="url(#poolTones)" role="img" aria-label="Render de villa de lujo con piscina y tarima de madera"/>
    </svg>

    <h1 class="headline">LOS PINOS DE ARENA</h1>
    <div class="headline-rule"></div>

    <p class="intro">
      <span>Compra tu segunda vivienda en un</span>
      <span>entorno privilegiado a unos pasos de</span>
      <span>una de las playas más bonitas de Cádiz.</span>
    </p>

    <div class="urgency-band"><p>NO TE LO PUEDES PERDER</p></div>

    <p class="details">30 villas de lujo en un terreno en primera línea de playa en el sur de España (Cádiz).</p>

    <div class="contact-box">
      <span class="contact-label">CONTACTO</span>
      <span class="contact-number">
        <svg viewBox="0 0 24 24" aria-hidden="true">
          <path d="M6.6 2.5c.5-.3 1.1-.2 1.4.3l2 3.2c.3.5.2 1.1-.2 1.4L8.4 8.5c.9 2.4 2.7 4.3 5.1 5.4l1.2-1.4c.4-.4 1-.5 1.4-.2l3.2 2c.5.3.6.9.3 1.4l-1.3 2.3c-.4.7-1.2 1-2 .8C10 17.5 5.6 13 4.4 7.4c-.2-.8.1-1.6.8-2z" fill="var(--blue)"/>
          <path d="M14 3.5a7 7 0 0 1 6.5 6.5M14 6.8a3.8 3.8 0 0 1 3.2 3.2" fill="none" stroke="var(--blue)" stroke-width="1.6" stroke-linecap="round"/>
        </svg>
        12345678A
      </span>
    </div>
  </section>
</body>
</html>
```